New Stationary for our business

We are a gift business and would like to create a new corporate image with new stationary and design.

We would like a Classic Corporate look with a touch of Flair.

We would need:
Envelopes
Letter Head
Business Cards
With Comp Slips
Note Pads
Etc...

Our details are:

Basket Haven Pty Ltd
518 Pelling Street, Carrow Vale, Victoria, 3071
1800 742 918
www.baskethaven.com.au
sales@baskethaven.com.au

ABN: 62 804 319 775

Target Market(s)

Corporate Look

Industry/Entity Type

Marketing

Contact Information for Business Card

Basket Haven Pty Ltd
1800 742 918
518 Pelling Street
Carrow Vale 3071
Victoria Australia

Darren Pelloni - Managing Director
darren.pelloni@baskethaven.com.au
0417 586 902

Logo Text

Basket Haven - The Present Experts

Colors

Designer to choose colors to be used in the design.

Requirements
Must have
• Look and Feel upmarket and exclusive

```html
<!DOCTYPE html>
<html lang="en">
<head>
<meta charset="utf-8">
<title>Basket Haven Stationery</title>
<link href="https://fonts.googleapis.com/css2?family=Montserrat:wght@400;600;700&family=Open+Sans:wght@400;600&display=swap" rel="stylesheet">
<style>
:root{
  --bg:#e3e7f1;
  --paper:#ffffff;
  --paper-soft:#f7f7f8;
  --teal:#3ccbc5;
  --teal-deep:#36c3c1;
  --grey:#9b9b9b;
  --ink:#3a3a3a;
  --ink-soft:#6b6b6b;
}
*{box-sizing:border-box;margin:0;padding:0}
html,body{width:1200px;height:1040px;overflow:hidden;background:var(--bg)}
body{position:relative;font-family:"Open Sans",sans-serif;color:var(--ink)}
.piece{position:absolute;background:var(--paper)}
.brand{display:flex;align-items:center;gap:4px;font-family:"Montserrat",sans-serif;font-weight:600;color:var(--teal);white-space:nowrap}
.brand .mark{display:block;background:var(--teal)}
.brand.on-teal{color:#fff}
.brand.on-teal .mark{background:#fff}

/* letterhead */
.letterhead{left:142px;top:101px;width:265px;height:374px}
.letterhead .brand{position:absolute;left:24px;top:20px;font-size:11px}
.letterhead .brand .mark{width:9px;height:9px}
.letter-body{position:absolute;left:27px;top:94px;width:212px;font-size:4.3px;line-height:5.6px;color:var(--ink)}
.letter-body p{margin-bottom:4px}
.signature{width:48px;height:10px;background:#e6e6e6;margin-top:6px}
.footer-line{position:absolute;left:0;right:0;bottom:10px;text-align:center;font-size:3.4px;line-height:4.5px;color:var(--ink-soft)}
.footer-line strong{color:var(--ink);font-weight:600}
.base-bar{position:absolute;left:0;right:0;bottom:0;height:3px;display:flex}
.base-bar .teal{flex:1;background:var(--teal)}
.base-bar .grey{width:45px;background:var(--grey)}

/* envelopes */
.envelope-front{left:466px;top:163px;width:278px;height:139px}
.envelope-front .brand{position:absolute;left:15px;top:18px;font-size:11px}
.envelope-front .brand .mark{width:9px;height:9px}
.return-address{position:absolute;left:15px;top:107px;font-size:3.6px;line-height:4.6px;color:var(--ink-soft)}
.return-address strong{color:var(--ink);font-weight:600}
.envelope-back{left:761px;top:162px;width:278px;height:139px}
.envelope-back svg{position:absolute;left:0;top:0}

/* notepad */
.notepad{left:474px;top:362px;width:267px;height:376px;background:var(--paper-soft)}
.notepad .brand{position:absolute;left:23px;top:21px;font-size:10.5px}
.notepad .brand .mark{width:9px;height:9px}
.notepad .footer-line{bottom:8px}

/* business cards */
.card{width:136px;height:79px;border-radius:5px;overflow:hidden}
.card-front{left:911px;top:382px;background:var(--teal)}
.card-front .brand{position:absolute;left:24px;top:30px;font-size:10px}
.card-front .brand .mark{width:8px;height:8px}
.card-front .web{position:absolute;left:0;right:0;top:64px;text-align:center;font-size:3.4px;color:#fff}
.card-back{left:911px;top:478px}
.card-back .brand{position:absolute;left:10px;top:11px;font-size:8px}
.card-back .brand .mark{width:7px;height:7px}
.card-person{position:absolute;left:14px;top:53px;font-size:4px;line-height:4.6px}
.card-person strong{font-weight:600}
.card-person span{display:block;font-size:3px;color:var(--ink-soft)}
.card-contact{position:absolute;left:68px;top:53px;font-size:2.8px;line-height:3.6px;color:var(--ink-soft)}
.card-contact .lines{margin-top:3px;padding-left:3px;border-left:1px solid var(--teal)}

/* presentation folder */
.folder{left:95px;top:530px;width:318px;height:399px;background:var(--teal-deep)}
.folder .brand{position:absolute;left:40px;top:172px;font-size:28px;gap:10px}
.folder .brand .mark{width:30px;height:30px}
.folder .web{position:absolute;left:0;right:0;top:374px;text-align:center;font-family:"Montserrat",sans-serif;font-weight:600;font-size:8px;color:#fff;letter-spacing:.2px}

/* compliments slip */
.comp-slip{left:474px;top:786px;width:266px;height:125px;background:var(--paper-soft)}
.comp-slip .brand{position:absolute;left:12px;top:22px;font-size:10.5px}
.comp-slip .brand .mark{width:9px;height:9px}
.comp-slip .greeting{position:absolute;right:14px;top:105px;font-family:"Montserrat",sans-serif;font-weight:600;font-size:12px;color:var(--teal)}

/* square card */
.square-card{left:786px;top:648px;width:156px;height:157px;background:var(--teal)}
.square-card .brand{position:absolute;left:26px;top:60px;font-size:10.5px}
.square-card .brand .mark{width:9px;height:9px}
.square-card .web{position:absolute;left:0;right:0;top:139px;text-align:center;font-size:3.4px;color:#fff}
</style>
</head>
<body>

<section class="piece letterhead">
  <div class="brand"><span class="mark"></span>Basket Haven</div>
  <div class="letter-body">
    <p>November 1, 2015<br>Mr. Colin Ashby<br>88 Quarry Lane<br>Fenwick, U.K 40210</p>
    <p>Dear Mr. Ashby<br>The first paragraph of a typical business letter is used to state the main point of the letter. Begin with a friendly opening, then quickly move into the purpose of your letter. Use a couple of sentences to explain the purpose, but do not go into detail until the next paragraph.</p>
    <p>Beginning with the second paragraph, state the supporting details to justify your purpose. These may take the form of background information, statistics or first-hand accounts. A few short paragraphs within the body of the letter should be enough to support your reasoning. Finally, in the closing paragraph, briefly restate your purpose and why it is important.</p>
    <p>Finally, in the closing paragraph, briefly restate your purpose and why it is important. If the purpose of your letter is related to your employment, consider ending your letter with your contact information and title if it is not included on letterhead.</p>
    <p>Finally, in the closing paragraph, briefly restate your purpose and why it is important. If the purpose of your letter is related to your employment, consider ending your letter with your contact information.</p>
    <p>Finally, in the closing paragraph, briefly restate your purpose and why it is important. If the purpose is informational, think about closing with gratitude for the reader's time.</p>
    <p>Sincerely,</p>
    <div class="signature" role="img" aria-label="Handwritten signature"></div>
    <p>President</p>
  </div>
  <div class="footer-line"><strong>Basket Haven Pty Ltd</strong><br>518 Pelling Street, Carrow Vale, Victoria, 3071 | Tel: 1800 742 918 | sales@baskethaven.com.au | ABN 62 804 319 775</div>
  <div class="base-bar"><span class="teal"></span><span class="grey"></span></div>
</section>

<section class="piece envelope-front">
  <div class="brand"><span class="mark"></span>Basket Haven</div>
  <div class="return-address"><strong>Basket Haven Pty Ltd</strong><br>518 Pelling Street,<br>Carrow Vale, Victoria, 3071<br>Tel: 1800 742 918</div>
</section>

<section class="piece envelope-back">
  <svg width="278" height="139" viewBox="0 0 278 139" aria-hidden="true">
    <polygon points="2,0 276,0 264,38 14,38" fill="#3ccbc5"/>
  </svg>
</section>

<section class="piece notepad">
  <div class="brand"><span class="mark"></span>Basket Haven</div>
  <div class="footer-line"><strong>Basket Haven Pty Ltd</strong><br>518 Pelling Street, Carrow Vale, Victoria, 3071 | Tel: 1800 742 918 | sales@baskethaven.com.au | ABN 62 804 319 775</div>
  <div class="base-bar"><span class="teal"></span><span class="grey"></span></div>
</section>

<section class="piece card card-front">
  <div class="brand on-teal"><span class="mark"></span>Basket Haven</div>
  <div class="web">www.baskethaven.com.au</div>
</section>

<section class="piece card card-back">
  <div class="brand"><span class="mark"></span>Basket Haven</div>
  <div class="card-person"><strong>Darren Pelloni</strong><span>Managing Director</span></div>
  <div class="card-contact">518 Pelling Street<br>Carrow Vale 3071, Victoria
    <div class="lines">0417 586 902<br>www.baskethaven.com.au<br>darren.pelloni@baskethaven.com.au</div>
  </div>
</section>

<section class="piece folder">
  <div class="brand on-teal"><span class="mark"></span>Basket Haven</div>
  <div class="web">www.baskethaven.com.au</div>
</section>

<section class="piece comp-slip">
  <div class="brand"><span class="mark"></span>Basket Haven</div>
  <div class="greeting">With Compliments</div>
</section>

<section class="piece square-card">
  <div class="brand on-teal"><span class="mark"></span>Basket Haven</div>
  <div class="web">www.baskethaven.com.au</div>
</section>

</body>
</html>
```